Career Counselor in need of a business card design

Hello Creatives! I'm in need of a business card design for a new company based in Georgia, USA called Pathways By Lantern.

Some things that may be helpful in creating your concept(s) include:

My Logo (Included in the Files section): There are three versions, two versions are in the second file. The all gold stacked (vertical) version is my primary logo and then there are two horizontal versions (one is all gold and the other is gold and grey).

My mission: to empower tweens through young adults to realize and actualize their CAREER ASPIRATIONS.
My vision: for tweens through young adults to LIVE LIFE ON PURPOSE and become CONTRIBUTING MEMBERS OF SOCIETY.

Biblical scriptures that support my ‘Why’: Psalms 127: 3-4(NIV) Children are a heritage from the Lord, offspring a reward from him. Like ARROWS in the hands of a warrior are children…. And Proverbs 29:18(JKV) Where there is no VISION, the people perish.

*Words in ALL CAPS are to emphasize what's important to me and may possibly provide you some inspiration (IDK - Have fun with it)!

Target Market(s)

My ideal customers are parents, guardians, and young adults.

Contact Information for Business Card

My name, degrees and credential: Delphine Marlow, M.S., Ed.S., NCC
Title: College and Career Coach and Consultant

Number: 555.318.2907
Address: 2718 Willowmere Avenue., Suite 405, Macon, GA 31299
Email: info@pathwaysbylantern.example
Website: www.pathwaysbylantern.example

My population: TWEENS • TEENS • EMERGING ADULTS
Services offered: One-On-One Sessions • Small Groups • Workshops

Colors

Designer to choose colors to be used in the design.

Requirements
Nice to have
• Either my mission or vision but I will understand if it does not all fit.
• My mission: To empower tweens through young adults to realize and actualize their career aspirations.
• My vision: For tweens through young adults to live life on purpose and become contributing members of society.

```html
<!DOCTYPE html>
<html lang="en">
<head>
<meta charset="utf-8">
<title>Pathways By Lantern – Business Card</title>
<link href="https://fonts.googleapis.com/css2?family=Cinzel:wght@500&family=Lato:wght@400;700&display=swap" rel="stylesheet">
<style>
  :root{
    --backdrop:#e4e4e6;
    --gold-light:#f6d462;
    --gold:#e0b23e;
    --gold-deep:#c8982f;
    --ink:#151515;
    --card-black:#1c1c1c;
    --card-black-edge:#252525;
    --text-soft:#d9d9d9;
    --accent-gold:#e8bd45;
  }
  *{box-sizing:border-box;margin:0;padding:0}
  html,body{width:1200px;height:900px;overflow:hidden}
  body{
    background:radial-gradient(ellipse at 40% 30%,#f2f2f3 0%,var(--backdrop) 70%);
    font-family:"Lato",Arial,sans-serif;
    position:relative;
  }
  .card{
    position:absolute;
    width:550px;height:314px;
    border-radius:26px;
    box-shadow:0 14px 30px rgba(0,0,0,.22);
    overflow:hidden;
  }
  /* front */
  .card--front{
    left:90px;top:100px;
    background:linear-gradient(160deg,var(--gold-deep) 0%,var(--gold) 35%,var(--gold-light) 70%,var(--gold) 100%);
    color:var(--ink);
  }
  .front-brand{
    position:absolute;left:0;right:0;top:96px;
    display:flex;flex-direction:column;align-items:center;gap:14px;
  }
  .brand-dot{
    width:54px;height:54px;border-radius:50%;
    border:5px solid var(--ink);
    flex:none;
  }
  .front-brand .brand-name{
    font-family:"Cinzel",Georgia,serif;font-weight:500;
    font-size:24px;letter-spacing:2px;color:var(--ink);
  }
  .services{
    position:absolute;left:0;right:0;bottom:34px;
    text-align:center;font-size:14px;letter-spacing:.6px;
    text-transform:uppercase;
  }
  /* back */
  .card--back{
    left:560px;top:470px;
    background:linear-gradient(150deg,var(--card-black-edge) 0%,var(--card-black) 60%,#121212 100%);
    color:var(--text-soft);
  }
  .lockup{
    position:absolute;left:34px;top:38px;
    display:flex;align-items:center;gap:14px;
  }
  .lockup .brand-dot{border-color:var(--accent-gold);width:40px;height:40px;border-width:4px}
  .lockup .brand-name{
    font-family:"Cinzel",Georgia,serif;font-weight:500;
    font-size:24px;letter-spacing:1.5px;color:var(--accent-gold);
  }
  .audience{
    position:absolute;left:34px;top:98px;
    font-size:12.5px;letter-spacing:.6px;text-transform:uppercase;color:var(--text-soft);
  }
  .address{
    position:absolute;right:34px;top:128px;text-align:right;
    font-size:13px;line-height:1.5;font-style:normal;
  }
  .person{position:absolute;left:34px;top:170px}
  .person-name{
    font-family:"Cinzel",Georgia,serif;font-weight:500;
    font-size:19px;color:var(--accent-gold);letter-spacing:.5px;
  }
  .person-title{font-size:14px;margin-top:2px}
  .contacts{position:absolute;left:34px;top:226px;list-style:none;font-size:14px;line-height:1.6}
  .contacts li{display:flex;align-items:center;gap:9px}
  .contacts svg{width:13px;height:13px;fill:var(--accent-gold)}
</style>
</head>
<body>

<section class="card card--front" aria-label="Card front">
  <div class="front-brand">
    <span class="brand-dot"></span>
    <span class="brand-name">PATHWAYS BY LANTERN</span>
  </div>
  <p class="services">One-On-One Sessions • Small Groups • Workshops</p>
</section>

<section class="card card--back" aria-label="Card back">
  <div class="lockup">
    <span class="brand-dot"></span>
    <span class="brand-name">PATHWAYS BY LANTERN</span>
  </div>
  <p class="audience">Tweens • Teens • Emerging Adults</p>
  <address class="address">
    2718 Willowmere Avenue<br>Suite 405, Macon, GA 31299
  </address>
  <div class="person">
    <p class="person-name">DELPHINE MARLOW, M.S., ED.S., NCC</p>
    <p class="person-title">College and Career Coach and Consultant</p>
  </div>
  <ul class="contacts">
    <li><svg viewBox="0 0 16 16" aria-hidden="true"><path d="M3 1h3l1.5 4-2 1.3a9 9 0 0 0 4.2 4.2L11 8.5l4 1.5v3a2 2 0 0 1-2 2A13 13 0 0 1 1 3a2 2 0 0 1 2-2z"/></svg>555.318.2907</li>
    <li><svg viewBox="0 0 16 16" aria-hidden="true"><path d="M1 3h14v10H1z M1.5 3.5 8 9l6.5-5.5" stroke="#1c1c1c" stroke-width="1.2"/></svg>info@pathwaysbylantern.example</li>
    <li><svg viewBox="0 0 16 16" aria-hidden="true"><circle cx="8" cy="8" r="7"/><path d="M1 8h14M8 1c-3 3-3 11 0 14M8 1c3 3 3 11 0 14" stroke="#1c1c1c" stroke-width="1" fill="none"/></svg>www.pathwaysbylantern.example</li>
  </ul>
</section>

</body>
</html>
```